Branvique needs a business Card Design

We are looking for a business card Design for our new Managed Service Provider Company, Branvique. Branvique encompasses everything IT for the average medium sized business. Our primary services are help desk support, cyber-security (malware and ransomware protection), and Disaster Recovery systems. We would like the design to have a very clean and professional look, with a very minimalist feel.

Target Market(s)

Medium to large sized businesses

Industry/Entity Type

It Service

Contact Information for Business Card

Name GoesHere
name@branvique.com
O: 555-382-6047
C: 555-731-5820

Font styles to use
Other font styles liked:
• Poppins Font Only Please

Colors

Designer to choose only greyscale colors for use in the design.

Requirements
Must have
• Logo included
Nice to have
• Cutting Edge, innovative, minimalistic, elegant

```html
<!DOCTYPE html>
<html lang="en">
<head>
<meta charset="utf-8">
<title>Branvique Business Card</title>
<link rel="stylesheet" href="https://fonts.googleapis.com/css2?family=Poppins:wght@300;400;500&display=swap">
<style>
  :root {
    --backdrop: #e9e9ea;
    --card-paper: #f7f7f7;
    --ink-navy: #06233f;
    --ink-dark: #111418;
    --ink-soft: #2b2f35;
    --ink-light: #f2f4f7;
  }
  * { box-sizing: border-box; margin: 0; padding: 0; }
  html, body {
    width: 1200px;
    height: 817px;
    overflow: hidden;
    background: var(--backdrop);
    font-family: "Poppins", sans-serif;
  }
  .card-sheet {
    position: relative;
    width: 1200px;
    height: 817px;
    display: flex;
    align-items: center;
    justify-content: center;
    gap: 40px;
  }
  .card {
    position: relative;
    width: 520px;
    height: 297px;
    background: var(--card-paper);
    box-shadow: 0 2px 6px rgba(0,0,0,0.12);
    overflow: hidden;
  }

  /* Front */
  .card-front__frame {
    position: absolute;
    inset: 22px 24px;
    border: 3px solid var(--ink-navy);
    display: flex;
    align-items: center;
    justify-content: center;
  }
  .brand-name {
    color: var(--ink-navy);
    font-weight: 400;
    font-size: 30px;
    letter-spacing: 0.36em;
    text-transform: uppercase;
    padding-left: 0.36em;
  }

  /* Back */
  .card-back__identity {
    position: absolute;
    left: 28px;
    top: 78px;
  }
  .person-name {
    color: var(--ink-dark);
    font-weight: 500;
    font-size: 23px;
    line-height: 1.2;
  }
  .person-role {
    color: var(--ink-dark);
    font-weight: 400;
    font-size: 13px;
    margin-top: 2px;
  }
  .person-email {
    color: var(--ink-soft);
    font-weight: 300;
    font-size: 10.5px;
    margin-top: 3px;
  }
  .card-back__sweep {
    position: absolute;
    inset: 0;
    width: 100%;
    height: 100%;
  }
  .card-back__sweep path { fill: var(--ink-navy); }
  .card-back__phones {
    position: absolute;
    right: 44px;
    bottom: 26px;
    color: var(--ink-light);
    font-weight: 300;
    font-size: 13px;
    line-height: 1.45;
  }
</style>
</head>
<body>
  <main class="card-sheet">
    <section class="card card-front" aria-label="Card front">
      <div class="card-front__frame">
        <span class="brand-name">Branvique</span>
      </div>
    </section>

    <section class="card card-back" aria-label="Card back">
      <svg class="card-back__sweep" viewBox="0 0 520 297" preserveAspectRatio="none" aria-hidden="true">
        <path d="M150 297 C 320 292 450 235 520 14 L520 297 Z"/>
      </svg>
      <div class="card-back__identity">
        <p class="person-name">Name goes here</p>
        <p class="person-role">Position/job</p>
        <p class="person-email">name@branvique.com</p>
      </div>
      <div class="card-back__phones">
        <p>O: 555-382-6047</p>
        <p>C: 555-731-5820</p>
      </div>
    </section>
  </main>
</body>
</html>
```